Webdesign für Helga Stirnweis, Corvell Management
Zielgruppe
Unternehmensberatung, Schwerpunkt Leadership development, Personalentwicklung und -beratung, Karrierecoaching, es soll auf jeder Seite auch ein link sein zur Englischseite;
ungefährer startseitetext: Mein Ziel: Begeistern und Befähigen;
Lernen und Veränderungen entstehen aus Reflexion. Der Betreffende tritt einen Schritt zurück, schaut auf das bisherige Verhalten und stellt sich die Frage, ob er dieses Verhalten und die Auswirkungen dieses Verhaltens in Zukunft wieder wählen möchten.
Leadership
• Fähigkeiten bei ihren MitarbeiterInnen aktivieren, welche sie sich selbst vielleicht nicht zugetraut hätten.
• Die Vielfalt unter ihren MitarabeiterInnen schätzen und die Unterschiede als Ressourcen nutzen.
• Eine Organisation schaffen, der ihre MitarbeiterInnen gerne angehören und in die sie gerne aktiv ihre Kompetenzen und ihr Potenzial einbringen.
Coaching:
Mein Ziel ist, Sie in ihren Herausforderung und Veränderungen zu unterstützen. Bei Veränderungen in ihrem beruflichen Werdegang oder den täglichen Herausforderungen, z.B. mit dem Zeitmanagement, werde ich Sie begleiten und beharrlich fordern.
Aufgabenstellung
es sollen Fotos (trainingsituationen) integriert werden, Schrift Geneva und Avenir Next gefallen mir, Logo vorhanden - in Farbe nachtblau/nightblue und schwarz;
gute Freunde beschreiben mich als: gewissenhaft, integrierend, beharrlich, ausdrucksstark, vertrauensvoll, offen, durchgreifend;

```html
<!DOCTYPE html>
<html lang="de">
<head>
<meta charset="utf-8">
<title>Helga Stirnweis – Corvell Management</title>
<link rel="stylesheet" href="https://fonts.googleapis.com/css2?family=Nunito+Sans:wght@300;400;600&display=swap">
<style>
:root{
  --night:#062a78;
  --card:#04296f;
  --accent:#0a8cff;
  --ink:#111a2b;
  --line:#2a4f9c;
  --footer:#002a7a;
  --bar:#000814;
  --white:#ffffff;
}
*{margin:0;padding:0;box-sizing:border-box}
html,body{width:763px;height:1200px;overflow:hidden;background:var(--white)}
body{font-family:"Nunito Sans",sans-serif;color:var(--ink);position:relative}
.page{position:relative;width:763px;height:1200px;overflow:hidden}

.hero-photo{position:absolute;left:0;top:0;width:763px;height:425px;
  background:radial-gradient(ellipse at 72% 40%,#c7a48e 0%,#8ea2bf 18%,rgba(160,205,230,0) 42%),
  linear-gradient(180deg,#d9eef8 0%,#bfe2f3 40%,#cfe8f4 80%,#ffffff 100%)}
.hero-fade{position:absolute;left:0;top:360px;width:763px;height:70px;background:linear-gradient(180deg,rgba(255,255,255,0),#fff)}

.header-line{position:absolute;top:43px;height:1px;background:var(--line)}
.logo{position:absolute;left:150px;top:17px;width:110px;color:var(--night);font-weight:400;line-height:1}
.logo-name{display:block;font-size:21px;letter-spacing:1px}
.logo-sub{display:block;font-size:7px;letter-spacing:6.2px;margin-top:5px}
.nav{position:absolute;top:27px;left:0;font-size:7px;color:var(--ink);letter-spacing:.2px}
.nav a{position:absolute;white-space:nowrap;color:inherit;text-decoration:none}

.hero-name{position:absolute;left:149px;top:204px;font-size:24px;font-weight:300;letter-spacing:.3px;color:var(--ink)}
.quote-mark{position:absolute;left:124px;top:238px;font-size:118px;line-height:1;font-weight:600;color:rgba(70,95,140,.35)}
.hero-quote{position:absolute;left:149px;top:256px;font-size:15.5px;line-height:20px;font-weight:300;color:var(--ink)}
.scroll-icon{position:absolute;left:376px;top:355px}

.section-title{position:absolute;left:0;width:763px;text-align:center;top:474px;font-size:24px;font-weight:300;letter-spacing:.3px}

.card{position:absolute;top:527px;width:136px;height:158px}
.card-frame{position:absolute;left:0;top:10px;width:124px;height:148px;border:1px solid var(--accent)}
.card-body{position:absolute;left:12px;top:0;width:122px;height:146px;background:var(--card);overflow:hidden}
.card-num{position:absolute;left:-6px;top:2px;font-size:58px;font-weight:600;color:rgba(120,140,190,.35);line-height:1}
.card-text{position:relative;padding:19px 8px 0 12px;color:var(--white);font-size:9.6px;line-height:14.5px;font-weight:400}
.card-check{position:absolute;left:4px;top:112px}

.city-photo{position:absolute;left:0;top:790px;width:763px;height:305px;
  background:linear-gradient(180deg,#e3f0f6 0%,#b8cdd6 18%,#8c9a9a 40%,#6e7e6e 70%,#5a6c58 100%)}
.city-fade{position:absolute;left:0;top:700px;width:763px;height:130px;background:linear-gradient(180deg,#fff 0%,rgba(236,245,250,.6) 60%,rgba(230,242,248,0) 100%)}

.contact-card{position:absolute;left:269px;top:724px;width:227px;height:290px;background:rgba(255,255,255,.86);text-align:center}
.contact-title{margin-top:24px;font-size:12px;font-weight:400;letter-spacing:.2px}
.contact-lead{width:150px;margin:6px auto 0;font-size:5.5px;line-height:9.6px}
.field{position:absolute;left:40px;width:147px;height:22px;background:var(--white);border:1px solid #d8dde4;font-size:5.5px;color:#8a9099;text-align:center;padding-top:7px}
.field-area{height:55px;padding-top:6px}
.submit{position:absolute;left:74px;top:248px;width:80px;height:22px;background:var(--accent);color:var(--white);font-size:7px;letter-spacing:.3px;line-height:22px}

.footer{position:absolute;left:0;top:1095px;width:763px;height:91px;background:var(--footer);color:var(--white);text-align:center;font-size:7px;line-height:14.5px;padding-top:23px}
.bottom-bar{position:absolute;left:0;top:1186px;width:763px;height:14px;background:var(--bar);color:var(--white);text-align:center;font-size:5.5px;line-height:14px}
</style>
</head>
<body>
<div class="page">
  <div class="hero-photo" role="img" aria-label="Foto: lächelnde Beraterin im Nadelstreifenblazer vor unscharfem Büro mit Kolleginnen"></div>
  <div class="hero-fade"></div>

  <div class="header-line" style="left:0;width:143px"></div>
  <div class="header-line" style="left:264px;width:499px"></div>
  <div class="logo"><span class="logo-name">CORVELL</span><span class="logo-sub">MANAGEMENT</span></div>
  <nav class="nav">
    <a style="left:308px">UNS</a>
    <a style="left:341px">1PRODUKTSEITEN</a>
    <a style="left:421px">2PRODUKTSEITEN</a>
    <a style="left:501px">3PRODUKTSEITEN</a>
    <a style="left:581px">KONTAKT</a>
  </nav>

  <h1 class="hero-name">HELGA STIRNWEIS</h1>
  <div class="quote-mark" aria-hidden="true">”</div>
  <p class="hero-quote">Mein Ziel ist, Sie in ihren Herausforderung<br>und Veränderungen zu unterstützen.</p>
  <svg class="scroll-icon" width="12" height="34" viewBox="0 0 12 34" aria-hidden="true">
    <rect x="1" y="1" width="10" height="16" rx="5" fill="none" stroke="#fff" stroke-width="1"/>
    <line x1="6" y1="4" x2="6" y2="8" stroke="#fff" stroke-width="1"/>
    <line x1="6" y1="20" x2="6" y2="33" stroke="#fff" stroke-width="1" stroke-dasharray="1.5 2"/>
  </svg>

  <h2 class="section-title">LEADERSHIP</h2>

  <div class="card" style="left:149px">
    <div class="card-frame"></div>
    <div class="card-body"><span class="card-num">01</span>
      <p class="card-text">Fähigkeiten bei ihren MitarbeiterInnen aktivieren, welche sie sich selbst vielleicht nicht zugetraut hätten.</p></div>
    <svg class="card-check" width="23" height="23" viewBox="0 0 23 23" aria-hidden="true"><circle cx="11.5" cy="11.5" r="10.5" fill="var(--accent)" stroke="#fff" stroke-width="1.5"/><path d="M6.5 11.8l3.3 3.3 6.5-6.6" fill="none" stroke="#fff" stroke-width="1.6"/></svg>
  </div>
  <div class="card" style="left:309px">
    <div class="card-frame"></div>
    <div class="card-body"><span class="card-num">02</span>
      <p class="card-text">Die Vielfalt unter ihren MitarabeiterInnen schätzen und die Unterschiede als Ressourcen nutzen.</p></div>
    <svg class="card-check" width="23" height="23" viewBox="0 0 23 23" aria-hidden="true"><circle cx="11.5" cy="11.5" r="10.5" fill="var(--accent)" stroke="#fff" stroke-width="1.5"/><path d="M6.5 11.8l3.3 3.3 6.5-6.6" fill="none" stroke="#fff" stroke-width="1.6"/></svg>
  </div>
  <div class="card" style="left:468px">
    <div class="card-frame"></div>
    <div class="card-body"><span class="card-num">03</span>
      <p class="card-text" style="padding-top:6px">Eine Organisation schaffen, der ihre MitarbeiterInnen gerne angehören und in die sie gerne aktiv ihre Kompetenzen und ihr Potenzial einbringen.</p></div>
    <svg class="card-check" width="23" height="23" viewBox="0 0 23 23" aria-hidden="true"><circle cx="11.5" cy="11.5" r="10.5" fill="var(--accent)" stroke="#fff" stroke-width="1.5"/><path d="M6.5 11.8l3.3 3.3 6.5-6.6" fill="none" stroke="#fff" stroke-width="1.6"/></svg>
  </div>

  <div class="city-photo" role="img" aria-label="Foto: Luftaufnahme einer Großstadt mit Hochhäusern und Grünflächen"></div>
  <div class="city-fade"></div>

  <form class="contact-card">
    <h3 class="contact-title">SCHREIBEN SIE UNS</h3>
    <p class="contact-lead">Lorem ipsum dolor sit amet, consectetur adipiscing elit. Integer faucibus ullaffsfhakkmcorper condimentum. Etiam vulputate anvbfffgte metus, hendrerit eleifend orci dictum malesuada.</p>
    <div class="field" style="top:93px">Name</div>
    <div class="field" style="top:122px">E-mail</div>
    <div class="field" style="top:151px">Telefon</div>
    <div class="field field-area" style="top:180px">Meldung</div>
    <div class="submit">SCHICKEN</div>
  </form>

  <footer class="footer">
    HelgaStirnweis@corvellmanagement.at<br>
    www.corvellmanagement.at<br>
    0043 660 482 17 395
  </footer>
  <div class="bottom-bar">CorvellManagement©Copyright2016</div>
</div>
</body>
</html>
```